Buchcover für ein Glücksbuch
Zielgruppe
Ich brauche ein Cover für mein Glücksbuch, es soll möglichst viele interessierte Leser ansprechen und zum Kauf des Buches animieren.
Mein Glücksbuch ist für jeden gedacht, der auch im Alltag in kleinen Dingen sein Glück sucht, es muss nicht immer das große Glück sein und auch Geld allein macht nicht glücklich. Es soll den Leser dazu bringen, das Glück in sich selbt zu finden. Es enthält Anleitungen und Tipps und eine Bonus-Mediation.
Aufgabenstellung
Der Titel des Buches lautet: 'Pfade zur Freude mit 12 Herzensfunken'
Untertitel: 'Heiter und gelassen jeden Tag mit Ideen und Übungen'
'Mit Bonus-Meditation'
Autorin (Pseudonym): Britta Wolder

```html
<!DOCTYPE html>
<html lang="de">
<head>
<meta charset="utf-8">
<title>Pfade zur Freude – Buchcover</title>
<link rel="stylesheet" href="https://fonts.googleapis.com/css2?family=Alegreya:wght@400;500&family=Oswald:wght@500&family=Roboto+Condensed:wght@400&display=swap">
<style>
  :root {
    --page-bg: #ecebea;
    --violet-deep: #5b2d8e;
    --violet-box: #6a3aa0;
    --violet-mid: #8a5cc4;
    --lilac: #b49ae0;
    --lilac-light: #d9cdf2;
    --white: #ffffff;
    --ladybug-red: #d8322a;
  }
  * { box-sizing: border-box; margin: 0; padding: 0; }
  html, body { width: 1200px; height: 800px; overflow: hidden; }
  body { background: var(--page-bg); position: relative; font-family: "Roboto Condensed", Arial, sans-serif; }

  .book-wrap {
    position: absolute; left: 105px; top: 50px;
    width: 990px; height: 700px;
    display: flex;
    box-shadow: 0 10px 30px rgba(60, 30, 90, 0.2);
  }

  /* Back cover */
  .back-cover {
    position: relative; width: 460px; height: 700px; overflow: hidden;
  }
  .flower-backdrop {
    position: absolute; inset: 0;
    background:
      radial-gradient(ellipse 40% 30% at 20% 85%, var(--lilac-light), transparent 70%),
      radial-gradient(ellipse 50% 35% at 80% 15%, var(--lilac), transparent 70%),
      radial-gradient(ellipse 45% 35% at 75% 75%, #9b6fd0, transparent 70%),
      linear-gradient(160deg, #a785dc 0%, var(--violet-mid) 45%, #b79ce3 100%);
  }
  .author-photo {
    position: absolute; left: 32px; top: 100px; width: 170px; height: 230px;
    background: linear-gradient(180deg, #c9c7c3 0%, #bdbab5 55%, #2f7a4a 56%, #256b3e 100%);
    z-index: 2;
  }
  .blurb-box {
    position: absolute; left: 150px; top: 135px; width: 290px; height: 520px;
    background: var(--violet-box); color: var(--white);
    padding: 18px 18px 18px 16px;
    font-size: 11.2px; line-height: 1.38; text-align: justify;
  }
  .blurb-box .photo-gap { float: left; width: 58px; height: 205px; }
  .blurb-box p + p { margin-top: 8px; }

  /* Spine */
  .spine {
    position: relative; width: 70px; height: 700px;
    background: linear-gradient(90deg, #6e3fa8, var(--violet-mid) 60%, #7b4cb6);
    color: var(--white);
  }
  .spine-title {
    position: absolute; left: 50%; top: 30px;
    writing-mode: vertical-rl; transform: translateX(-50%) rotate(180deg);
    height: 540px; text-align: center;
    font-family: "Alegreya", Georgia, serif; font-size: 33px; white-space: nowrap;
    rotate: 180deg;
  }
  .spine-author {
    position: absolute; left: 0; right: 0; bottom: 24px; text-align: center;
    font-family: "Oswald", "Arial Narrow", sans-serif; font-weight: 500; font-size: 20px; line-height: 1.1;
  }

  /* Front cover */
  .front-cover {
    position: relative; width: 460px; height: 700px; overflow: hidden; color: var(--white);
  }
  .cover-photo {
    position: absolute; inset: 0;
    background:
      radial-gradient(ellipse 14% 16% at 62% 52%, var(--ladybug-red), transparent 75%),
      radial-gradient(ellipse 30% 25% at 55% 62%, #7a4fc0, transparent 70%),
      radial-gradient(ellipse 35% 25% at 15% 70%, var(--lilac-light), transparent 70%),
      radial-gradient(ellipse 40% 30% at 90% 30%, var(--lilac), transparent 70%),
      linear-gradient(170deg, #8e62cc 0%, #9f78d6 50%, #a98ade 100%);
  }
  .cover-title {
    position: absolute; right: 36px; top: 60px; text-align: right;
    font-family: "Alegreya", Georgia, serif; font-weight: 400;
  }
  .title-main { font-size: 74px; line-height: 0.95; }
  .title-line { display: flex; align-items: flex-end; justify-content: flex-end; gap: 6px; margin-top: 10px; }
  .title-mit { font-size: 38px; padding-bottom: 6px; }
  .title-number { font-size: 110px; line-height: 0.8; font-weight: 500; }
  .title-sparks { font-size: 34px; align-self: flex-start; padding-top: 4px; }
  .cover-author {
    position: absolute; right: 60px; top: 275px;
    font-family: "Oswald", "Arial Narrow", sans-serif; font-weight: 500; font-size: 26px;
  }
  .bonus-badge { position: absolute; right: 18px; top: 410px; width: 120px; height: 120px; }
  .cover-subtitle {
    position: absolute; left: 30px; right: 30px; bottom: 70px; text-align: center;
    font-family: "Alegreya", Georgia, serif; font-size: 25px; line-height: 1.25;
  }
</style>
</head>
<body>
  <div class="book-wrap">
    <section class="back-cover">
      <div class="flower-backdrop" role="img" aria-label="Unscharfe Fliederblüten in Violett und Lila"></div>
      <div class="blurb-box">
        <div class="photo-gap"></div>
        <p>In den 25 Jahren meiner selbständigen Arbeit als Hebamme, habe ich viele Familien im Wochenbett betreut und dabei einen reichen Erfahrungsschatz gesammelt. Meine häufigsten Kunden waren natürlich Familien, die das erste Kind bekommen haben.</p>
        <p>Dies war zu der Zeit, als gerade der Krankenhausaufenthalt nach einer Spontangeburt von zehn auf sieben Tage gekürzt worden war. Die Krankenkasse bezahlte im Anschluss daran vier Tage Hebammen-Betreuung. Wenn die Familie diverse schwierige Themenfelder hatte, übernahm die Kasse die Kosten auch länger.</p>
        <p>Da ich meinen Beruf liebte, nahm ich mir für den Wochenbettbesuch auch immer genügend Zeit. Meist war eine Stunde nötig, manchmal jedoch waren so viele Fragen oder Irritationen (Unklarheiten), daß ich länger blieb. Auf die frisch gebackenen Eltern kommen unzählige unbekannte Situationen zu, die total verunsichern können. Auch bei sehr einfühlsamer Betreuung im Krankenhaus stellen sich viele Fragen erst zu Hause. Nämlich dann, wenn der Alltag mit dem Baby beginnt.</p>
      </div>
      <div class="author-photo" role="img" aria-label="Porträtfoto der Autorin in grüner Bluse vor grauem Hintergrund"></div>
    </section>

    <section class="spine">
      <div class="spine-title">Pfade zur Freude mit 12 Herzensfunken</div>
      <div class="spine-author">Britta<br>Wolder</div>
    </section>

    <section class="front-cover">
      <div class="cover-photo" role="img" aria-label="Marienkäfer auf violetten Fliederblüten, unscharfer lila Hintergrund"></div>
      <h1 class="cover-title">
        <span class="title-main">Pfade zur<br>Freude</span>
        <span class="title-line">
          <span class="title-mit">mit</span>
          <span class="title-number">12</span>
          <span class="title-sparks">Herzensfunken</span>
        </span>
      </h1>
      <div class="cover-author">Britta Wolder</div>
      <svg class="bonus-badge" viewBox="0 0 120 120" aria-label="Mit Bonus-Meditation">
        <defs>
          <path id="badge-arc" d="M 60 60 m -44 0 a 44 44 0 1 0 88 0 a 44 44 0 1 0 -88 0"/>
        </defs>
        <circle cx="60" cy="60" r="57" fill="var(--violet-deep)" stroke="var(--lilac-light)" stroke-width="2"/>
        <text font-family="Oswald, sans-serif" font-weight="500" font-size="14" fill="#ffffff" letter-spacing="1.5">
          <textPath href="#badge-arc" startOffset="4%">Mit Bonus-Meditation</textPath>
        </text>
        <circle cx="60" cy="60" r="16" fill="var(--ladybug-red)"/>
      </svg>
      <p class="cover-subtitle">Heiter und gelassen jeden Tag mit<br>Ideen und Übungen</p>
    </section>
  </div>
</body>
</html>
```